Business card for home decor store and design

I need a business card for my home decor boutique that’s professional looking boho/rustic. We sell vintage furniture, vintage finds, lamps, throws, rugs. We also carry a Diy paint line for refinishing furniture. We offer workshop on painting furniture, private or group setting. We in the heart of Old Town Red Bluff. We love to design, build and restore. Family owned small business. Our style is rustic boho farmhouse. We search for one of a kind found and repurposed items. We love vintage home decor, vintage windows.

Target Market(s)

Home decor

Industry/Entity Type

Home Accessories

Contact Information for Business Card

Have a rustic look/boho

Font styles to use
Serif
Script

Requirements
Must have
• Logo

```html
<!DOCTYPE html>
<html lang="en">
<head>
<meta charset="utf-8">
<title>Birch &amp; Hearth Co. — Business Card</title>
<link href="https://fonts.googleapis.com/css2?family=Montserrat:wght@400;500&family=Dancing+Script:wght@600&display=swap" rel="stylesheet">
<style>
  :root {
    --backdrop: #3b3b3c;
    --card: #141414;
    --gold: #c99a62;
    --gold-soft: #b9895a;
  }
  * { margin: 0; padding: 0; box-sizing: border-box; }
  html, body { width: 799px; height: 1200px; overflow: hidden; }
  body {
    background: var(--backdrop);
    display: flex;
    flex-direction: column;
    align-items: center;
    justify-content: center;
    gap: 110px;
    font-family: "Montserrat", sans-serif;
    color: var(--gold);
  }
  .card {
    width: 640px;
    height: 366px;
    background: var(--card);
    border-radius: 6px;
    box-shadow: 0 14px 30px rgba(0,0,0,.45);
    position: relative;
  }
  .card-front {
    display: flex;
    align-items: center;
    justify-content: center;
  }
  .brand {
    display: flex;
    align-items: center;
    gap: 12px;
    font-family: "Montserrat", sans-serif;
    font-weight: 500;
    color: var(--gold);
    white-space: nowrap;
  }
  .brand-dot {
    width: 14px; height: 14px;
    border-radius: 50%;
    background: var(--gold);
    flex: none;
  }
  .card-front .brand { font-size: 34px; }
  .card-back .brand {
    position: absolute;
    left: 36px; top: 166px;
    font-size: 22px;
  }
  .contact {
    position: absolute;
    left: 340px; top: 96px;
  }
  .contact-name {
    font-family: "Dancing Script", cursive;
    font-size: 34px;
    line-height: 1;
    color: var(--gold);
  }
  .contact-title {
    font-size: 14px;
    margin-top: 6px;
    color: var(--gold-soft);
  }
  .contact-list { list-style: none; margin-top: 16px; }
  .contact-list li {
    display: flex;
    align-items: center;
    gap: 12px;
    font-size: 15px;
    line-height: 24px;
  }
  .contact-list svg { width: 13px; height: 13px; flex: none; }
  .contact-address {
    font-size: 15px;
    line-height: 22px;
    margin-top: 6px;
    font-style: normal;
  }
</style>
</head>
<body>
  <section class="card card-front">
    <div class="brand"><span class="brand-dot"></span>Birch &amp; Hearth Co.</div>
  </section>

  <section class="card card-back">
    <div class="brand"><span class="brand-dot"></span>Birch &amp; Hearth Co.</div>
    <div class="contact">
      <p class="contact-name">Jane Roe Miller</p>
      <p class="contact-title">Managing Director</p>
      <ul class="contact-list">
        <li>
          <svg viewBox="0 0 16 16" aria-hidden="true"><path fill="currentColor" d="M3.5 1h3l1 4-2 1.2a9 9 0 0 0 4.3 4.3L11 8.5l4 1v3A2.5 2.5 0 0 1 12.5 15 11.5 11.5 0 0 1 1 3.5 2.5 2.5 0 0 1 3.5 1z"/></svg>
          555-010-2040
        </li>
        <li>
          <svg viewBox="0 0 16 16" aria-hidden="true"><rect x="1" y="3" width="14" height="10" rx="1" fill="currentColor"/><path d="M1.5 3.8 8 9l6.5-5.2" fill="none" stroke="#141414" stroke-width="1.4"/></svg>
          jane@birchhearth.com
        </li>
        <li>
          <svg viewBox="0 0 16 16" aria-hidden="true"><g fill="none" stroke="currentColor" stroke-width="1.4"><circle cx="8" cy="8" r="6.5"/><ellipse cx="8" cy="8" rx="3" ry="6.5"/><path d="M1.5 8h13"/></g></svg>
          www.birchhearth.com
        </li>
      </ul>
      <address class="contact-address">418 Maple Row, Fairview,<br>Hill County, US 102938</address>
    </div>
  </section>
</body>
</html>
```